New London Job Board - Business Card Required

Dear All,

I own Quintaro Limited, which in turn owns the website:
www.brambletopfield.com

I want all of you wonderful creative people to come up with a slick, and awesome business card design that incorporates the logo on the site, and some colouring and design elements from it.

You have free reign in how you go about doing this, I won't be giving my contact details on this platform, but the winner will be asked to redesign based on my contact details which I will supply at the end.

I need the design to be completed within 5 days. I need the final print copies of the business cards by the 25th November, so unfortunately it's a bit of a rush to get these designs ready.

Any questions, please ask.

Thank you

Thank you all for your hard work and exceptional designs provided. I do have to pick one, so I have a very clear idea of which one this is, however I will wait one further day until the competition closes to be fair to all those have submitted, or are in the process of submitting. I wish you all the best and thank you again for your dedication.

```html
<!DOCTYPE html>
<html lang="en">
<head>
<meta charset="utf-8">
<title>Brambletop Field – Business Card</title>
<link rel="stylesheet" href="https://fonts.googleapis.com/css2?family=Carlito:wght@400;700&display=swap">
<style>
  :root {
    --stage: #e8e5e0;
    --card-black: #0c0c0c;
    --card-charcoal: #242424;
    --gold-light: #f3d27a;
    --gold: #d9a93c;
    --gold-deep: #9a6512;
    --gold-text: #e0b04a;
    --gold-muted: #c9962f;
  }
  * { margin: 0; padding: 0; box-sizing: border-box; }
  html, body {
    width: 1200px; height: 538px; overflow: hidden;
    background: var(--stage);
    font-family: "Carlito", "Calibri", sans-serif;
  }
  .canvas { position: relative; width: 1200px; height: 538px; }
  .card-sheet {
    position: absolute; left: 0; top: 0; width: 470px; height: 538px;
  }
  .card-face {
    position: absolute; left: 0; width: 470px; overflow: hidden;
    color: var(--gold-text); text-align: center;
  }
  .card-front { top: 0; height: 268px; }
  .card-back { top: 268px; height: 270px; border-top: 1px solid #000; }
  .damask-fill {
    position: absolute; inset: 0;
    background: radial-gradient(ellipse at 50% 45%, var(--card-charcoal) 0%, var(--card-black) 85%);
  }
  .card-content { position: relative; height: 100%; }

  .brand-block { position: absolute; left: 0; right: 0; top: 0; height: 268px; }
  .brand-mark {
    position: absolute; left: 50%; top: 58px; width: 96px; height: 96px;
    margin-left: -48px; border-radius: 50%; background: var(--gold);
  }
  .brand-rule {
    position: absolute; left: 104px; width: 262px; height: 2px;
    background: linear-gradient(90deg, var(--gold-deep), var(--gold-light), var(--gold-deep));
  }
  .brand-rule.upper { top: 193px; }
  .brand-rule.lower { top: 232px; }
  .brand-name {
    position: absolute; left: 0; right: 0; top: 199px;
    font-size: 27px; font-weight: 400; letter-spacing: 1.5px;
    color: var(--gold-text); text-transform: uppercase;
  }

  .holder-name {
    position: absolute; left: 0; right: 0; top: 24px;
    font-size: 27px; font-weight: 700; color: var(--gold-text);
  }
  .holder-role {
    position: absolute; left: 0; right: 0; top: 60px;
    font-size: 15px; font-weight: 700; color: var(--gold-muted);
  }
  .gold-band {
    position: absolute; left: 0; width: 466px; height: 6px;
    background: linear-gradient(90deg, var(--gold-deep), var(--gold) 40%, var(--gold-light) 70%, var(--gold-deep));
  }
  .gold-band.upper { top: 88px; }
  .gold-band.lower { top: 184px; }
  .contact-line {
    position: absolute; left: 0; right: 0;
    font-size: 22px; font-weight: 700; color: var(--gold-text);
  }
  .contact-line.email { top: 105px; }
  .contact-line.web { top: 137px; }
  .address-line {
    position: absolute; left: 0; right: 0;
    font-size: 16px; font-weight: 700; color: var(--gold-muted);
  }
  .address-line.street { top: 212px; }
  .address-line.phone { top: 234px; }
</style>
</head>
<body>
<main class="canvas">
  <section class="card-sheet" aria-label="Business card, front and back">
    <article class="card-face card-front">
      <div class="damask-fill" role="img" aria-label="Black damask flourish pattern background"></div>
      <div class="card-content brand-block">
        <span class="brand-mark" aria-hidden="true"></span>
        <span class="brand-rule upper"></span>
        <h1 class="brand-name">Brambletop Field</h1>
        <span class="brand-rule lower"></span>
      </div>
    </article>
    <article class="card-face card-back">
      <div class="damask-fill" role="img" aria-label="Black damask flourish pattern background"></div>
      <div class="card-content">
        <h2 class="holder-name">Tarin Okafor</h2>
        <p class="holder-role">Managing Director</p>
        <span class="gold-band upper"></span>
        <p class="contact-line email">contact@brambletopfield.com</p>
        <p class="contact-line web">www.brambletopfield.com</p>
        <span class="gold-band lower"></span>
        <p class="address-line street">27 Larkspur Row, Halden, LD4 9QT</p>
        <p class="address-line phone">0700 555 0192</p>
      </div>
    </article>
  </section>
</main>
</body>
</html>
```